MS Word Template needed for a company specialized in network and security infrastructures

We need a new MS Word Template. <br/>Our activity is services in IT (network infrastructure and security). We usually use french language. <br/>The template must be nice and beautiful, and easy to use. If possible, try to use as less as possible text zones to simplify redaction tasks. And try to use "native" polices in MS Word. I attached sample documents for example. Please try to use the same colour codes.

Target Market(s)

Consulting in Network and security domain

Industry/Entity Type

It Service

Colors

Designer to choose colors to be used in the design.

Requirements
Must have
• - Nice design
• - Easy to use
• - very professional aspect
Nice to have
• - actual ox relay solutions logo
• - actual colour code

```html
<!DOCTYPE html>
<html lang="en">
<head>
<meta charset="utf-8">
<title>Ox Relay Solutions – Word Template</title>
<link href="https://fonts.googleapis.com/css2?family=Montserrat:wght@300;400;500;700;800&display=swap" rel="stylesheet">
<style>
:root{
  --bg:#9b9b9b;
  --green:#72bf7f;
  --teal:#2a9bb5;
  --deep-teal:#2d5f63;
  --navy:#0f2a40;
  --ink:#0d2b3e;
  --text:#33414a;
  --muted:#8a959c;
  --rule:#c9cfd3;
  --row-green:#e3f2e5;
  --row-teal:#d6eef4;
}
*{margin:0;padding:0;box-sizing:border-box}
html,body{width:1200px;height:2400px;overflow:hidden;background:var(--bg);font-family:"Montserrat",Arial,sans-serif;color:var(--text)}
.canvas{position:relative;width:1200px;height:2400px}
.page{position:absolute;width:526px;height:745px;background:#fff;box-shadow:6px 8px 14px rgba(0,0,0,.35);overflow:hidden}
.page--cover{left:351px;top:25px;background:linear-gradient(160deg,#2d6466,#173a4e)}
.page--contents{left:51px;top:813px}
.page--body{left:625px;top:813px}
.page--body2{left:51px;top:1601px}
.page--back{left:625px;top:1601px;background:linear-gradient(160deg,#245a5c 0%,#173f52 45%,#10263f 100%)}
.abs{position:absolute}

/* cover */
.cover-inner{position:absolute;left:8px;top:8px;width:510px;height:729px;background:#fff;overflow:hidden}
.cover-art{position:absolute;left:0;top:0}
.cover-dots{position:absolute;left:31px;top:527px;display:flex;gap:4px}
.cover-dots span{width:10px;height:10px;border-radius:50%}
.cover-title{position:absolute;left:29px;top:546px;font-weight:800;font-size:42px;letter-spacing:.5px;color:var(--ink);line-height:1}
.cover-subtitle{position:absolute;left:31px;top:596px;font-weight:400;font-size:16px;color:var(--teal);letter-spacing:.3px}
.brand{position:absolute;display:flex;align-items:center;gap:7px;font-weight:500;color:var(--teal);letter-spacing:.6px;text-transform:uppercase;white-space:nowrap}
.brand-dot{border-radius:50%;background:var(--green);flex:none}
.brand--cover{right:16px;bottom:30px;font-size:13px}
.brand--cover .brand-dot{width:22px;height:22px}

/* header band & footer */
.band{position:absolute;left:0;top:0;width:100%;height:19px;background:linear-gradient(90deg,var(--green),var(--teal))}
.band--rev{background:linear-gradient(90deg,var(--teal),var(--green))}
.footer-rule{position:absolute;top:720px;height:1px;background:var(--rule)}
.page-num{position:absolute;top:713px;width:15px;height:13px;background:var(--teal);color:#fff;font-size:7px;text-align:center;line-height:13px;border-radius:1px}
.brand--foot{top:714px;font-size:5.5px;gap:3px}
.brand--foot .brand-dot{width:10px;height:10px}

/* contents */
.toc-title{position:absolute;left:33px;top:44px;font-size:12px;font-weight:500;color:var(--green);font-variant:small-caps;letter-spacing:.4px}
.toc{position:absolute;left:33px;width:461px;display:flex;align-items:baseline;font-size:11px;font-weight:400;color:var(--ink)}
.toc .num{width:31px;flex:none}
.toc .lead{flex:1;border-bottom:1px dotted #666;margin:0 2px;transform:translateY(-3px)}
.toc--sub{font-size:8.5px;color:#555}
.toc--sub .lead{border-bottom-style:dashed;border-color:#999}
.toc--sub3{color:#888}

/* headings */
.h1{position:absolute;left:32px;width:464px;font-weight:700;font-size:17px;color:var(--ink);border-bottom:2px solid var(--ink);padding-bottom:2px;letter-spacing:.3px}
.h2{position:absolute;left:32px;font-weight:700;font-size:13.5px;color:var(--deep-teal);letter-spacing:.4px}
.h3{position:absolute;left:32px;font-size:10px;font-weight:400;color:var(--teal);letter-spacing:.4px}
.h4{position:absolute;left:32px;font-size:9px;font-weight:300;color:var(--green);letter-spacing:.4px}
.h5{position:absolute;left:32px;font-size:9px;font-weight:400;color:var(--ink)}
.h3 span,.h4 span,.h5 span{display:inline-block;width:26px;font-weight:inherit}
.h4 span{width:32px}
.h5 span{width:38px}

/* tables */
.data-table{position:absolute;left:32px;width:464px;border-collapse:collapse;font-size:8.5px;line-height:10.5px}
.data-table th{font-weight:300;color:#fff;text-align:left;padding:0 4px}
.data-table td{padding:0 4px;color:var(--ink);border-bottom:1px solid #fff}
.data-table--green th{background:var(--green)}
.data-table--green tbody tr:nth-child(odd) td{border-bottom:1px solid var(--green)}
.data-table--green tbody tr:nth-child(2) td{background:var(--row-green);border-bottom:1px solid var(--green)}
.data-table--teal th{background:var(--teal)}
.data-table--teal tbody tr:nth-child(odd) td{border-bottom:1px solid var(--teal)}
.data-table--teal tbody tr:nth-child(2) td{background:var(--row-teal);border-bottom:1px solid var(--teal)}

.chart-title{position:absolute;font-size:12px;color:#555;transform:translateX(-50%)}
.legend{position:absolute;display:flex;gap:9px;font-size:7.5px;color:#666;transform:translateX(-50%);white-space:nowrap}
.legend i{display:inline-block;width:4px;height:4px;margin-right:2px;vertical-align:middle}

/* bullets */
.bullet{position:absolute;font-size:9px;color:var(--ink);display:flex;align-items:center;white-space:nowrap}
.bullet::before{content:"";width:8px;height:8px;border-radius:50%;margin-right:9px;background:var(--teal)}
.bullet--num::before{width:6px;height:6px;background:var(--deep-teal);margin-right:11px}
.bullet--sub::before{width:3px;height:3px;background:var(--green);margin-right:12px}

.brand--back{left:50%;top:650px;transform:translateX(-50%);font-size:11px;color:#fff}
.brand--back .brand-dot{width:26px;height:26px}
</style>
</head>
<body>
<div class="canvas">

  <!-- Cover -->
  <section class="page page--cover">
    <div class="cover-inner">
      <svg class="cover-art" width="510" height="510" viewBox="0 0 510 510" role="img" aria-label="Photograph of a person touching a digital network of connected user and gear icons, with a tablet showing charts">
        <defs>
          <linearGradient id="coverBlue" x1="0" y1="0" x2="1" y2="1">
            <stop offset="0" stop-color="#3a63a8"/>
            <stop offset=".5" stop-color="#2a62b0"/>
            <stop offset="1" stop-color="#163668"/>
          </linearGradient>
          <linearGradient id="coverLight" x1="0" y1="0" x2="1" y2="1">
            <stop offset="0" stop-color="#e6edf5"/>
            <stop offset="1" stop-color="#4f79a8"/>
          </linearGradient>
        </defs>
        <polygon points="0,0 510,0 510,505 0,153" fill="url(#coverBlue)"/>
        <polygon points="0,162 325,383 0,505" fill="url(#coverLight)"/>
      </svg>
      <div class="cover-dots"><span style="background:var(--green)"></span><span style="background:var(--teal)"></span><span style="background:var(--deep-teal)"></span></div>
      <h1 class="cover-title">TITLE HERE</h1>
      <p class="cover-subtitle">SUBTITLE HERE</p>
      <div class="brand brand--cover"><span class="brand-dot"></span>Ox Relay Solutions</div>
    </div>
  </section>

  <!-- Contents -->
  <section class="page page--contents">
    <div class="band"></div>
    <div class="toc-title">Contents</div>
    <div class="toc" style="top:66px"><span class="num">1</span>HEADING 01<span class="lead"></span>3</div>
    <div class="toc toc--sub" style="top:82px"><span class="num">1.1</span>HEADING 02<span class="lead"></span>3</div>
    <div class="toc toc--sub toc--sub3" style="top:96px"><span class="num">1.1.1</span>HEADING 03<span class="lead"></span>3</div>
    <div class="toc" style="top:116px"><span class="num">2</span>TABLE 01<span class="lead"></span>3</div>
    <div class="toc toc--sub" style="top:132px"><span class="num">2.1</span>TABLE 02<span class="lead"></span>3</div>
    <div class="toc" style="top:147px"><span class="num">3</span>Chart<span class="lead"></span>3</div>
    <div class="toc" style="top:163px"><span class="num">4</span>Bullet list<span class="lead"></span>4</div>
    <div class="brand brand--foot" style="left:16px"><span class="brand-dot"></span>Ox Relay Solutions</div>
    <div class="footer-rule" style="left:68px;width:418px"></div>
    <div class="page-num" style="left:485px">2</div>
  </section>

  <!-- Body page 3 -->
  <section class="page page--body">
    <div class="band band--rev"></div>
    <h2 class="h1" style="top:50px">1&nbsp; HEADING 01</h2>
    <h3 class="h2" style="top:99px">1.1&nbsp; HEADING 02</h3>
    <h4 class="h3" style="top:141px"><span>1.1.1</span>HEADING 03</h4>
    <h5 class="h4" style="top:177px"><span>1.1.1.1</span>HEADING 04</h5>
    <h6 class="h5" style="top:213px"><span>1.1.1.1.1</span>Heading 05</h6>

    <h2 class="h1" style="top:251px">2&nbsp; TABLE 01</h2>
    <table class="data-table data-table--green" style="top:282px">
      <thead><tr><th>Versão</th><th>Data</th><th>Autor</th><th>Comentários</th><th>Elaborado/modificado</th></tr></thead>
      <tbody>
        <tr><td>1,00</td><td>00</td><td>000</td><td>Original</td><td>000</td></tr>
        <tr><td>2.00</td><td>000</td><td>00</td><td>Original</td><td>000</td></tr>
        <tr><td>000</td><td>000</td><td>000</td><td>000</td><td>000</td></tr>
      </tbody>
    </table>

    <h3 class="h2" style="top:344px">2.1 TABLE 02</h3>
    <table class="data-table data-table--teal" style="top:369px">
      <thead><tr><th>Versão</th><th>Data</th><th>Autor</th><th>Comentários</th><th>Elaborado/modificado</th></tr></thead>
      <tbody>
        <tr><td>1,00</td><td>00</td><td>000</td><td>Original</td><td>000</td></tr>
        <tr><td>2.00</td><td>000</td><td>00</td><td>Original</td><td>000</td></tr>
        <tr><td>000</td><td>000</td><td>000</td><td>000</td><td>000</td></tr>
      </tbody>
    </table>

    <h2 class="h1" style="top:437px">3&nbsp; Chart</h2>
    <div class="chart-title" style="left:272px;top:477px">Sales</div>
    <svg class="abs" style="left:196px;top:506px" width="152" height="152" viewBox="0 0 152 152">
      <g transform="rotate(-90 76 76)" fill="none" stroke-width="13">
        <circle cx="76" cy="76" r="63" pathLength="100" stroke="var(--green)" stroke-dasharray="57.6 42.4" stroke-dashoffset="0"/>
        <circle cx="76" cy="76" r="63" pathLength="100" stroke="var(--teal)" stroke-dasharray="22.6 77.4" stroke-dashoffset="-58"/>
        <circle cx="76" cy="76" r="63" pathLength="100" stroke="var(--deep-teal)" stroke-dasharray="9.6 90.4" stroke-dashoffset="-81"/>
        <circle cx="76" cy="76" r="63" pathLength="100" stroke="var(--navy)" stroke-dasharray="8.6 91.4" stroke-dashoffset="-91"/>
      </g>
      <g font-family="Montserrat, Arial, sans-serif" font-size="6.5" fill="#fff" text-anchor="middle">
        <text x="139" y="93">58%</text>
        <text x="14" y="97">23%</text>
        <text x="24" y="41">10%</text>
        <text x="58" y="19">9%</text>
      </g>
    </svg>
    <div class="legend" style="left:272px;top:677px">
      <span><i style="background:var(--green);border-radius:50%"></i>1st Qtr</span>
      <span><i style="background:var(--teal);border-radius:50%"></i>2nd Qtr</span>
      <span><i style="background:var(--deep-teal);border-radius:50%"></i>3rd Qtr</span>
      <span><i style="background:var(--navy);border-radius:50%"></i>4th Qtr</span>
    </div>

    <div class="page-num" style="left:27px">3</div>
    <div class="footer-rule" style="left:52px;width:418px"></div>
    <div class="brand brand--foot" style="right:16px"><span class="brand-dot"></span>Ox Relay Solutions</div>
  </section>

  <!-- Body page 4 -->
  <section class="page page--body2">
    <div class="band"></div>
    <div class="chart-title" style="left:270px;top:72px;font-size:13px">Chart Title</div>
    <svg class="abs" style="left:0;top:0" width="526" height="290" viewBox="0 0 526 290">
      <defs>
        <linearGradient id="barGreen" x1="0" y1="0" x2="0" y2="1"><stop offset="0" stop-color="#7cc98a"/><stop offset="1" stop-color="#5daf6d"/></linearGradient>
        <linearGradient id="barTeal" x1="0" y1="0" x2="0" y2="1"><stop offset="0" stop-color="#45b1c7"/><stop offset="1" stop-color="#2289a3"/></linearGradient>
        <linearGradient id="barDark" x1="0" y1="0" x2="0" y2="1"><stop offset="0" stop-color="#3e6f74"/><stop offset="1" stop-color="#2a565b"/></linearGradient>
      </defs>
      <g stroke="#d9dde0" stroke-width="1">
        <line x1="98" y1="98" x2="452" y2="98"/><line x1="98" y1="123.3" x2="452" y2="123.3"/>
        <line x1="98" y1="148.6" x2="452" y2="148.6"/><line x1="98" y1="174" x2="452" y2="174"/>
        <line x1="98" y1="199.3" x2="452" y2="199.3"/><line x1="98" y1="224.6" x2="452" y2="224.6"/>
        <line x1="98" y1="250" x2="452" y2="250"/>
      </g>
      <g font-family="Montserrat, Arial, sans-serif" font-size="7.5" fill="#666" text-anchor="end">
        <text x="91" y="101">6</text><text x="91" y="126">5</text><text x="91" y="152">4</text>
        <text x="91" y="177">3</text><text x="91" y="202">2</text><text x="91" y="228">1</text><text x="91" y="253">0</text>
      </g>
      <g>
        <rect x="110" y="141" width="20" height="109" fill="url(#barGreen)"/>
        <rect x="134" y="189" width="20" height="61" fill="url(#barTeal)"/>
        <rect x="158" y="199" width="20" height="51" fill="url(#barDark)"/>
        <rect x="198.5" y="187" width="20" height="63" fill="url(#barGreen)"/>
        <rect x="222.5" y="139" width="20" height="111" fill="url(#barTeal)"/>
        <rect x="246.5" y="199" width="20" height="51" fill="url(#barDark)"/>
        <rect x="287" y="161" width="20" height="89" fill="url(#barGreen)"/>
        <rect x="311" y="204" width="20" height="46" fill="url(#barTeal)"/>
        <rect x="335" y="174" width="20" height="76" fill="url(#barDark)"/>
        <rect x="375.5" y="136" width="20" height="114" fill="url(#barGreen)"/>
        <rect x="399.5" y="179" width="20" height="71" fill="url(#barTeal)"/>
        <rect x="423.5" y="123" width="20" height="127" fill="url(#barDark)"/>
      </g>
      <g font-family="Montserrat, Arial, sans-serif" font-size="7.5" fill="#777" text-anchor="middle">
        <text x="142" y="263">Category 1</text><text x="231" y="263">Category 2</text>
        <text x="320" y="263">Category 3</text><text x="408" y="263">Category 4</text>
      </g>
    </svg>
    <div class="legend" style="left:270px;top:276px">
      <span><i style="background:var(--green)"></i>Series 1</span>
      <span><i style="background:var(--teal)"></i>Series 2</span>
      <span><i style="background:var(--deep-teal)"></i>Series 3</span>
    </div>

    <h2 class="h1" style="left:33px;top:320px">4&nbsp; Bullet list</h2>
    <div class="bullet" style="left:35px;top:366px">ORS Bullet 1</div>
    <div class="bullet" style="left:35px;top:383px">ORS Bullet 2</div>
    <div class="bullet" style="left:35px;top:401px">ORS Bullet 3</div>
    <div class="bullet" style="left:35px;top:418px">ORS Bullet 4</div>
    <div class="bullet" style="left:35px;top:435px">ORS Bullet 5</div>

    <div class="bullet bullet--num" style="left:51px;top:479px">ORS Numbered Bullet 1</div>
    <div class="bullet bullet--sub" style="left:97px;top:494px">ORS Numbered Bullet 1</div>
    <div class="bullet bullet--num" style="left:51px;top:508px">ORS Numbered Bullet 1</div>
    <div class="bullet bullet--sub" style="left:97px;top:523px">ORS Numbered Bullet 1</div>
    <div class="bullet bullet--num" style="left:51px;top:538px">ORS Numbered Bullet 1</div>
    <div class="bullet bullet--sub" style="left:97px;top:553px">ORS Numbered Bullet 1</div>

    <div class="brand brand--foot" style="left:16px"><span class="brand-dot"></span>Ox Relay Solutions</div>
    <div class="footer-rule" style="left:68px;width:418px"></div>
    <div class="page-num" style="left:485px">4</div>
  </section>

  <!-- Back cover -->
  <section class="page page--back">
    <div class="brand brand--back"><span class="brand-dot"></span>Ox Relay Solutions</div>
  </section>

</div>
</body>
</html>
```